The Quiet Ascent Book Cover

Book Title:
The Quiet Ascent: Lessons of Insight From A Circle of Mentors to Guide You Toward a Fuller Journey

This book will offer the wisdom and philosophies of a variety of different coaches to allow future clients to get a taste of you and your style and prepare them to work with you!

A coach does not fix you. Or heal you. They coach you - offer thoughts to ponder, guidance, techniques to try. All to help you plays and succeed at the game of life.

Each coach has their own personality, training, experience, method and philosophy they bring to the table. The underlying purpose is to guide you through The Quiet Ascent, to become the person you desire and aspire to be. Different coaches for different folks, yet they all have their own unique wisdom and special sauce to share.

This book is a collection of just that. A tasting of the wisdom and philosophies of a variety of different coaches for you to experience.

Types of Coaches: Clarity, Dreams, Goals, Motivation, Mindset,  Subconscious, Beliefs, Behavior, Accountability, Life, Wellness, Love & Dating, Relationships, Sex, Business, Career,  Executive,  Personal Development,  Writing, Wellness, Fitness, Parenting,  Style, Spirituality, Public Speaking, Financial,  Time management, Weight Loss, Running, Self esteem,  Tarot, Astrology, Enneagram, Soul path/ Dharma, Skills, Performance,  Speaking / Communication, Leadership, Shadow Work, Acting, Sports, ANY & ALL

Target Market(s)

Males or females looking for guidance and words of wisdom from an expert coach - maybe to find one that resonates with them to work with further. Ages 16 and up. Any Gender. International. Looking to improve their life!

Industry/Entity Type

Self Development, Wellness, Coaching, Personal Growth, Fitness, Spirituality, Business, Relationships

Font styles to use
Serif
Script

Colors
0054AA
0677BA
7BADD7
CADEEF
E8F1F8
FFF300
FFF600
FEFA6F
FFFEC7
FFFEE8

Requirements
Must have
• I am looking for a visually appealing, unique cover that encompasses the breadth and depth of the transformation that people can go through and inspires them to want to grow and change even more. I love when elegant and classic simplicity is combined with some kind of twist that catches the eye and provokes thought. I love complimentary fonts, colors, design elements. You can visit my Veltrano Author Page - Dr. Marisol Penbury Aldane to see my titles to see what I have liked! But I am also excited to see where you can make my vision even better!!
Nice to have
• Front Cover - Image, Title and Subtitle, The Lark Publishing House, Spine - Title and Publishing House Logo, Back - Book Blurb, Authors Names, Info about Publishing House, ISBN Barcode
Should not have
• Anything too feminine or too masculine as I want to encourage coaches of all genders to participate.

```html
<!DOCTYPE html>
<html lang="en">
<head>
<meta charset="utf-8">
<title>The Quiet Ascent — Book Cover</title>
<link rel="stylesheet" href="https://fonts.googleapis.com/css2?family=Russo+One&display=swap">
<style>
  :root {
    --page-bg: #ecebe8;
    --cover-bg: #ffffff;
    --ink-grey: #58595c;
    --art-lavender: #a9a3cf;
    --art-violet: #8a5bb0;
    --art-blue: #8fa6d2;
    --circle-white: #fdfdfb;
  }
  * { margin: 0; padding: 0; box-sizing: border-box; }
  html, body {
    width: 1036px;
    height: 1200px;
    overflow: hidden;
    background: var(--page-bg);
  }
  .book-cover {
    position: absolute;
    left: 128px;
    top: 15px;
    width: 780px;
    height: 1170px;
    background: var(--cover-bg);
    overflow: hidden;
    box-shadow: 0 2px 10px rgba(0,0,0,0.12);
  }
  .cover-art {
    position: absolute;
    inset: 0;
    width: 780px;
    height: 1170px;
  }
  .title-block {
    position: absolute;
    left: 140px;
    top: 268px;
    width: 500px;
    text-align: center;
    color: var(--ink-grey);
    font-family: "Russo One", sans-serif;
  }
  .book-title {
    font-weight: 400;
    font-size: 70px;
    line-height: 0.98;
    letter-spacing: 1px;
    text-transform: uppercase;
  }
  .book-subtitle {
    margin: 26px auto 0;
    width: 400px;
    font-size: 19px;
    line-height: 1.3;
    text-transform: uppercase;
    letter-spacing: 0.3px;
  }
  .publisher-name {
    position: absolute;
    left: 0;
    width: 100%;
    top: 1010px;
    text-align: center;
    font-family: "Russo One", sans-serif;
    font-size: 36px;
    letter-spacing: 1px;
    color: var(--ink-grey);
    text-transform: uppercase;
  }
</style>
</head>
<body>
  <main class="book-cover">
    <svg class="cover-art" viewBox="0 0 780 1170">
      <defs>
        <linearGradient id="artTone" x1="0" y1="0" x2="1" y2="1">
          <stop offset="0%" stop-color="var(--art-blue)"/>
          <stop offset="50%" stop-color="var(--art-violet)"/>
          <stop offset="100%" stop-color="var(--art-lavender)"/>
        </linearGradient>
      </defs>
      <rect class="art-area" x="0" y="40" width="780" height="950" fill="url(#artTone)"
            role="img" aria-label="Watercolour splash illustration in violet, lavender and blue with colourful butterflies around a central circle"/>
      <circle class="title-circle" cx="390" cy="450" r="258" fill="var(--circle-white)"/>
    </svg>

    <header class="title-block">
      <h1 class="book-title">The<br>Quiet<br>Ascent</h1>
      <p class="book-subtitle">Lessons of Insight From A Circle of Mentors to Guide You Toward a Fuller Journey</p>
    </header>

    <p class="publisher-name">The Lark Publishing House</p>
  </main>
</body>
</html>
```